Wedding poster templates PSD format

Create a range of editable wedding templates for different themes. Must be able able to adjust layers and edit all text.
Must include Names and dates for example purposes.
These are to be used as print templates for our wedding clients so we must be able to edit in photoshop.

We would like to see designs will be perfect for our customers to keep as a memento from their wedding or provided as a gift to be kept and remembered

Also needs to specific scale 1250mm high x 450mm wide

We have attached a sample of one of our designs. We would like similar designs to example.

Some attached links also show the style and look we are after.

Some nice silhouette type images to suit the chosen theme.

http://www.velquoriath.com/wp-content/uploads/2012/06/nautical_BrindleFernwick.jpg

http://www.gossamerpennyhollows.com/wp-content/uploads/2012/07/IMG_3168C.jpg

Themes we would like as ideas
Hawaii, Beach, Vintage, Floral, Tropical, Country, Garden, Nautical

Target Market(s)

Wedding

Industry/Entity Type

Wedding

Font styles to use
Decorative

Requirements
Must have
• Theme, Layers, Text, Names example, Dates example
Nice to have
• Silhouettes,
• Word cloud,
• Poem
• Vector images
Should not have
• Too much colour.
• Photographic images

```html
<!DOCTYPE html>
<html lang="en">
<head>
<meta charset="utf-8">
<title>Wedding Ticket Invitation – Elena &amp; Theo</title>
<link rel="stylesheet" href="https://fonts.googleapis.com/css2?family=Alfa+Slab+One&family=Rye&family=Ultra&display=swap">
<style>
  :root {
    --parchment-light: #e6cf9f;
    --parchment: #c9a66d;
    --parchment-dark: #6e4c27;
    --ink: #1e1912;
    --ink-shadow: #3b2a17;
    --wine: #7a1a16;
    --emerald: #2c7a5d;
    --emerald-dark: #1d5241;
    --cream: #efdcb4;
  }
  html, body {
    margin: 0;
    padding: 0;
    width: 1200px;
    height: 432px;
    overflow: hidden;
    background: #f2eee6;
  }
  .ticket {
    position: relative;
    width: 1200px;
    height: 432px;
    overflow: hidden;
    background:
      radial-gradient(ellipse 70% 60% at 50% 50%, var(--parchment-light) 0%, rgba(201,166,109,0.6) 55%, rgba(110,76,39,0) 100%),
      radial-gradient(ellipse 30% 25% at 20% 70%, rgba(120,80,40,0.25), transparent 70%),
      radial-gradient(ellipse 25% 30% at 80% 30%, rgba(120,80,40,0.2), transparent 70%),
      radial-gradient(ellipse 120% 120% at 50% 50%, var(--parchment) 40%, var(--parchment-dark) 100%);
    font-family: "Times New Roman", Times, serif;
    color: var(--ink);
  }
  .abs { position: absolute; }
  .display-layer { position: absolute; left: 0; top: 0; }

  /* frame */
  .frame { left: 5px; top: 5px; width: 1186px; height: 418px; border: 2px solid var(--ink); }
  .stub-edge { left: 303px; top: 6px; width: 2px; height: 420px; background: var(--ink); }
  .tear-line { left: 296px; top: 8px; height: 416px; border-left: 1.5px dashed var(--wine); }

  /* stub */
  .stub-rule-v { top: 30px; width: 2px; height: 372px; background: var(--ink); }
  .stub-rule-v.left { left: 68px; }
  .stub-rule-v.right { left: 286px; }
  .stub-rule-h { left: 118px; width: 136px; height: 2px; background: var(--ink); }
  .stub-date, .stub-couple {
    left: 72px; width: 214px; text-align: center;
    font-size: 21px; line-height: 1; color: var(--emerald-dark); letter-spacing: 0.5px;
  }
  .stub-date { top: 30px; }
  .stub-couple { top: 382px; }
  .save-the-date {
    left: 34px; top: 222px; width: 326px;
    display: flex; justify-content: space-between; align-items: center;
    transform: translate(-50%, -50%) rotate(90deg);
  }
  .save-the-date .letter {
    width: 21px; height: 21px; border-radius: 50%;
    background: var(--ink-shadow);
    color: var(--wine);
    font-size: 14px; font-weight: bold; line-height: 21px; text-align: center;
    box-shadow: 0 0 0 1px var(--wine);
  }
  .save-the-date .gap { width: 14px; }

  /* ornaments (placeholders) */
  .ornament { background: radial-gradient(ellipse at center, rgba(40,28,16,0.35), rgba(40,28,16,0) 70%); }

  /* display type (svg) */
  .type-rye { font-family: "Rye", "Alfa Slab One", serif; }
  .type-ultra { font-family: "Ultra", "Alfa Slab One", serif; }
  .type-slab { font-family: "Alfa Slab One", "Ultra", serif; }
  .type-serif { font-family: "Times New Roman", Times, serif; }

  .rule { height: 3px; background: var(--ink); }
  .divider-v { left: 523px; top: 252px; width: 3px; height: 132px; background: var(--ink); }
  .city { left: 744px; top: 362px; width: 214px; text-align: center; font-size: 22px; line-height: 1; letter-spacing: 1px; white-space: nowrap; }
</style>
</head>
<body>
<main class="ticket">
  <div class="abs frame"></div>
  <div class="abs tear-line"></div>
  <div class="abs stub-edge"></div>

  <section class="stub">
    <div class="abs stub-rule-v left"></div>
    <div class="abs stub-rule-v right"></div>
    <div class="abs save-the-date" aria-label="Save the date">
      <span class="letter">S</span><span class="letter">A</span><span class="letter">V</span><span class="letter">E</span>
      <span class="gap"></span>
      <span class="letter">T</span><span class="letter">H</span><span class="letter">E</span>
      <span class="gap"></span>
      <span class="letter">D</span><span class="letter">A</span><span class="letter">T</span><span class="letter">E</span>
    </div>
    <div class="abs stub-date">October 1st 2016</div>
    <div class="abs stub-rule-h" style="top:58px"></div>
    <div class="abs stub-rule-h" style="top:370px"></div>
    <div class="abs stub-couple">Elena &amp; Theo</div>
  </section>

  <section class="invitation">
    <div class="abs ornament" style="left:308px;top:8px;width:68px;height:60px" role="img" aria-label="Corner flourish ornament"></div>
    <div class="abs ornament" style="left:1088px;top:8px;width:100px;height:60px" role="img" aria-label="Corner flourish ornament"></div>
    <div class="abs ornament" style="left:308px;top:352px;width:66px;height:70px" role="img" aria-label="Corner flourish ornament"></div>
    <div class="abs ornament" style="left:1100px;top:352px;width:88px;height:70px" role="img" aria-label="Corner flourish ornament"></div>
    <div class="abs ornament" style="left:340px;top:112px;width:100px;height:26px" role="img" aria-label="Scroll flourish"></div>
    <div class="abs ornament" style="left:1058px;top:112px;width:100px;height:26px" role="img" aria-label="Scroll flourish"></div>
    <div class="abs ornament" style="left:388px;top:312px;width:92px;height:20px" role="img" aria-label="Small scroll flourish"></div>

    <div class="abs rule" style="left:356px;top:192px;width:776px"></div>
    <div class="abs rule" style="left:356px;top:241px;width:776px"></div>
    <div class="abs divider-v"></div>
    <div class="abs rule" style="left:556px;top:345px;width:576px"></div>
    <div class="abs city">Montreal, Quebec</div>
  </section>

  <svg class="display-layer" width="1200" height="432" viewBox="0 0 1200 432">
    <!-- stub: admit one -->
    <g class="type-rye">
      <text transform="translate(104,76) rotate(90)" font-size="132" textLength="276" lengthAdjust="spacingAndGlyphs" fill="var(--ink-shadow)" dx="3" dy="-3">ONE</text>
      <text transform="translate(104,76) rotate(90)" font-size="132" textLength="276" lengthAdjust="spacingAndGlyphs" fill="var(--ink)" stroke="var(--cream)" stroke-width="1.2">ONE</text>
      <text transform="translate(212,76) rotate(90)" font-size="82" textLength="224" lengthAdjust="spacingAndGlyphs" fill="var(--ink-shadow)" dx="3" dy="-3">ADMIT</text>
      <text transform="translate(212,76) rotate(90)" font-size="82" textLength="224" lengthAdjust="spacingAndGlyphs" fill="var(--ink)" stroke="var(--cream)" stroke-width="1">ADMIT</text>
    </g>

    <!-- heading -->
    <text class="type-slab" x="574" y="52" font-size="30" fill="var(--wine)">You're Invited<tspan class="type-serif" font-size="17" dx="8">to the</tspan></text>

    <g fill="var(--emerald)" stroke="var(--emerald-dark)" stroke-width="1">
      <polygon transform="translate(436,100)" points="24,0 30,17 48,17 34,28 39,46 24,35 9,46 14,28 0,17 18,17"/>
      <polygon transform="translate(1014,100)" points="24,0 30,17 48,17 34,28 39,46 24,35 9,46 14,28 0,17 18,17"/>
    </g>

    <text class="type-rye" x="500" y="160" font-size="104" textLength="496" lengthAdjust="spacingAndGlyphs" fill="var(--ink-shadow)">WEDDING</text>
    <text class="type-rye" x="496" y="156" font-size="104" textLength="496" lengthAdjust="spacingAndGlyphs" fill="var(--ink)" stroke="var(--cream)" stroke-width="1.4">WEDDING</text>

    <g fill="none" stroke="var(--wine)" stroke-width="1.4">
      <g transform="translate(620,164)">
        <polygon points="9,0 11.2,6 17.5,6 12.4,9.8 14.3,16 9,12.3 3.7,16 5.6,9.8 0.5,6 6.8,6"/>
        <polygon transform="translate(25,0)" points="9,0 11.2,6 17.5,6 12.4,9.8 14.3,16 9,12.3 3.7,16 5.6,9.8 0.5,6 6.8,6"/>
        <polygon transform="translate(50,0)" points="9,0 11.2,6 17.5,6 12.4,9.8 14.3,16 9,12.3 3.7,16 5.6,9.8 0.5,6 6.8,6"/>
        <polygon transform="translate(75,0)" points="9,0 11.2,6 17.5,6 12.4,9.8 14.3,16 9,12.3 3.7,16 5.6,9.8 0.5,6 6.8,6"/>
      </g>
      <g transform="translate(778,164)">
        <polygon points="9,0 11.2,6 17.5,6 12.4,9.8 14.3,16 9,12.3 3.7,16 5.6,9.8 0.5,6 6.8,6"/>
        <polygon transform="translate(25,0)" points="9,0 11.2,6 17.5,6 12.4,9.8 14.3,16 9,12.3 3.7,16 5.6,9.8 0.5,6 6.8,6"/>
        <polygon transform="translate(50,0)" points="9,0 11.2,6 17.5,6 12.4,9.8 14.3,16 9,12.3 3.7,16 5.6,9.8 0.5,6 6.8,6"/>
        <polygon transform="translate(75,0)" points="9,0 11.2,6 17.5,6 12.4,9.8 14.3,16 9,12.3 3.7,16 5.6,9.8 0.5,6 6.8,6"/>
      </g>
    </g>
    <text class="type-serif" x="752" y="178" font-size="18" text-anchor="middle" fill="var(--wine)">of</text>

    <!-- couple -->
    <text class="type-ultra" x="384" y="228" font-size="24" textLength="724" lengthAdjust="spacingAndGlyphs"><tspan fill="var(--emerald)">Elena</tspan><tspan fill="var(--wine)">Castillo</tspan><tspan class="type-rye" fill="var(--emerald)" font-size="30" dx="22">&amp;</tspan><tspan fill="var(--emerald)" dx="22">Theo</tspan><tspan fill="var(--wine)">Andrakis</tspan></text>

    <!-- day block -->
    <text class="type-serif" x="390" y="292" font-size="22" text-anchor="middle" fill="var(--wine)">the</text>
    <text class="type-rye" x="435" y="311" font-size="78" text-anchor="middle" fill="var(--ink)" stroke="var(--cream)" stroke-width="1">1</text>
    <text class="type-serif" x="462" y="292" font-size="20" text-anchor="middle" fill="var(--wine)">st</text>
    <text class="type-serif" x="421" y="352" font-size="15" text-anchor="middle" fill="var(--wine)">of</text>
    <text class="type-serif" x="430" y="370" font-size="22" text-anchor="middle" letter-spacing="1" fill="var(--wine)" transform="rotate(-9 430 362)">OCTOBER</text>

    <!-- venue -->
    <text class="type-rye" x="573" y="317" font-size="46" textLength="548" lengthAdjust="spacingAndGlyphs" fill="var(--ink)">THE SILVER PAVILION</text>
    <text class="type-rye" x="570" y="314" font-size="46" textLength="548" lengthAdjust="spacingAndGlyphs" fill="var(--emerald)" stroke="var(--cream)" stroke-width="1.2">THE SILVER PAVILION</text>
  </svg>
</main>
</body>
</html>
```